New banner graphics for Kelbro.com website

I've developed a software tool that helps businesses ensure they are working on their most valuable and important work.

I would like a banner graphic for my home page (www.kelbro.com) that can somehow capture the value of focus and intentional outcomes.

I had an initial thought of a starry sky that shifts focus to a few bright stars, but while that might sound ok, I think my idea is lame hence I'm coming to you guys.

My sites two primary colors are a soft purple and gray.
#919EC1(purple)
#9E9E9E (gray)

Target Market(s)

B2B for enterprises. Typical customers are CFOs, CIOs/Heads of IT

Industry/Entity Type

Business Software

Number of Pages Required

1 page

Font styles to use
Sans Serif

Colors
b8a6cd
cedeed

Requirements
Must have
• I use Divi as my Wordpress theme and the current main landing page can be seen at www.kelbro.com.
• My logo colors are:
• #919EC1(purple)
• #9E9E9E (gray)
Should not have
• Lots of distraction or visual "noise". I want to re-enforce the message that my software is focused on their business and not my products or website.

```html
<!DOCTYPE html>
<html lang="en">
<head>
<meta charset="UTF-8">
<title>Business Strategy Banner</title>
<link href="https://fonts.googleapis.com/css2?family=Roboto:wght@700&family=Raleway:ital,wght@0,400;0,800;1,700;1,800&display=swap" rel="stylesheet">
<style>
  :root {
    --sky-deep: #071a2e;
    --sky-mid: #0d3350;
    --sky-teal: #15606a;
    --text-white: #ffffff;
    --frame-line: rgba(255, 255, 255, 0.75);
  }
  html, body {
    margin: 0;
    padding: 0;
    overflow: hidden;
    background: var(--sky-deep);
  }
  .banner {
    position: relative;
    width: 1200px;
    height: 675px;
    overflow: hidden;
    color: var(--text-white);
  }
  .banner__sky {
    position: absolute;
    inset: 0;
    background:
      radial-gradient(ellipse 45% 35% at 45% 85%, rgba(32, 130, 130, 0.55), transparent 70%),
      radial-gradient(ellipse 50% 40% at 20% 25%, rgba(40, 100, 140, 0.45), transparent 70%),
      radial-gradient(ellipse 60% 50% at 70% 50%, rgba(20, 70, 110, 0.5), transparent 75%),
      linear-gradient(135deg, var(--sky-mid) 0%, var(--sky-deep) 55%, #06121f 100%);
  }
  .headline {
    position: absolute;
    top: 130px;
    left: 0;
    width: 100%;
    height: 68px;
    margin: 0;
    font-family: "Roboto", Arial, sans-serif;
    font-weight: 700;
    font-size: 47px;
    line-height: 68px;
  }
  .headline__lead {
    position: absolute;
    left: 295px;
    top: 0;
  }
  .headline__frame {
    position: absolute;
    left: 477px;
    top: 0;
    width: 461px;
    height: 69px;
    box-sizing: border-box;
    border: 1px solid var(--frame-line);
    text-align: center;
    white-space: nowrap;
  }
  .checklist {
    position: absolute;
    top: 296px;
    left: 0;
    width: 100%;
    margin: 0;
    padding: 0;
    list-style: none;
    font-family: "Raleway", Arial, sans-serif;
    font-size: 27.5px;
    line-height: 34px;
    text-transform: uppercase;
  }
  .checklist__row {
    display: flex;
    justify-content: center;
    align-items: baseline;
    white-space: nowrap;
  }
  .checklist__good { font-weight: 800; }
  .checklist__or {
    font-weight: 400;
    text-transform: none;
    margin: 0 20px;
  }
  .checklist__bad {
    font-weight: 700;
    font-style: italic;
  }
</style>
</head>
<body>
  <main class="banner">
    <div class="banner__sky" role="img" aria-label="Photograph of a deep blue and teal night sky full of stars"></div>

    <h1 class="headline">
      <span class="headline__lead">Is Your</span>
      <span class="headline__frame">“ Business Strategy ”</span>
    </h1>

    <ul class="checklist">
      <li class="checklist__row"><span class="checklist__good">Written down</span><span class="checklist__or">or</span><span class="checklist__bad">Loose thoughts – on the best of days.</span></li>
      <li class="checklist__row"><span class="checklist__good">Driving projects</span><span class="checklist__or">or</span><span class="checklist__bad">Just a set of slides tacked to walls</span></li>
      <li class="checklist__row"><span class="checklist__good">Shared with the team</span><span class="checklist__or">or</span><span class="checklist__bad">Kept top secret just to be safe</span></li>
      <li class="checklist__row"><span class="checklist__good">Measurable</span><span class="checklist__or">or</span><span class="checklist__bad">More art than science</span></li>
    </ul>
  </main>
</body>
</html>
```